Haventrix Corporate Stationery

Look for design of all new corporate stationery for an existing insurance broking business that is going through a redesign and move from older partners to younger family members. New Logo is attached. Company is Brisbane based.
Colours in the Logo is Hex #43bed8 and website features a lot of hex #17b8d8. Website front page "A plan to protect you" - headline. "Professional and Individual advice to protect your greatest assets" - tagline.

Stationery required: Business Cards, Letter head, Thank-you cards, Birthday cards, Presentation folders, With Compliment slips and a powerpoint template. We also would like to send a card to all customers with the something along of the lines of "something new".

Target Market(s)

Customers of Insurance business looking at superannuation, life and income protection insurance, investment advice and wills

Industry/Entity Type

Insurance Broker

Font styles to use
Other font styles liked:
• same as logo

Requirements
Must have
• The above designs for new stationery for the new business including:
• Business Cards, Letter head, Thank-you cards, Birthday cards, Presentation folders, With Compliment slips and a powerpoint template. We also would like to send a card to all customers with the something along of the lines of "something new".
Nice to have
• It is a new look - long time family business being passed to next generation - big focus on advice for YOU, individual advice etc..

```html
<!DOCTYPE html>
<html lang="en">
<head>
<meta charset="utf-8">
<title>Haventrix Business Card</title>
<link rel="stylesheet" href="https://fonts.googleapis.com/css2?family=Open+Sans:wght@400;600;700&display=swap">
<style>
  :root {
    --brand: #3fbfd9;
    --ink: #555a5e;
    --grey: #7d8084;
    --paper: #ffffff;
    --backdrop: #2b2b2b;
  }
  * { margin: 0; padding: 0; box-sizing: border-box; }
  html, body { width: 1200px; height: 987px; overflow: hidden; }
  body {
    background: var(--backdrop);
    font-family: "Open Sans", Arial, sans-serif;
    position: relative;
  }
  .card {
    position: absolute;
    left: 293px;
    width: 615px;
    height: 352px;
  }
  .card--front { top: 130px; background: var(--paper); }
  .card--back { top: 505px; background: var(--brand); }

  .brand {
    position: absolute;
    display: flex;
    align-items: center;
    gap: 14px;
  }
  .brand__dot {
    width: 58px; height: 58px;
    border-radius: 50%;
  }
  .brand__name {
    font-weight: 600;
    letter-spacing: 2px;
  }
  .card--front .brand { left: 31px; top: 49px; }
  .card--front .brand__dot { background: var(--grey); }
  .card--front .brand__name { color: var(--brand); font-size: 30px; }

  .card--back .brand {
    left: 50%; top: 50%;
    transform: translate(-50%, -50%);
    gap: 18px;
  }
  .card--back .brand__dot { width: 78px; height: 78px; background: var(--paper); }
  .card--back .brand__name { color: var(--paper); font-size: 38px; }

  .address {
    position: absolute;
    left: 31px; top: 145px;
    font-size: 15.5px;
    line-height: 23.4px;
    color: var(--ink);
  }
  .contacts {
    position: absolute;
    left: 31px; top: 199px;
    list-style: none;
    font-size: 15.5px;
    line-height: 23.4px;
    color: var(--ink);
  }
  .contacts li { display: flex; align-items: center; gap: 8px; }
  .contacts svg { width: 15px; height: 15px; flex: none; fill: var(--brand); }

  .nameplate {
    position: absolute;
    left: 405px; top: 209px;
    width: 210px; height: 55px;
    background: var(--brand);
    color: var(--paper);
    padding: 4px 0 0 28px;
  }
  .nameplate__name { font-size: 19px; font-weight: 700; line-height: 24px; letter-spacing: 0.3px; }
  .nameplate__role { font-size: 15px; line-height: 20px; padding-left: 16px; }
</style>
</head>
<body>
  <section class="card card--front">
    <div class="brand">
      <span class="brand__dot"></span>
      <span class="brand__name">HAVENTRIX</span>
    </div>

    <p class="address">42 Wattle Grove Road<br>Brisbane, QLD 4000</p>

    <ul class="contacts">
      <li>
        <svg viewBox="0 0 16 16" aria-hidden="true"><path d="M3.6 1.2l2.3 2.6-1.2 1.9c.9 2 2.6 3.7 4.6 4.6l1.9-1.2 2.6 2.3-1.4 2.6C7.2 14 2 8.8 1 3.6z"/></svg>
        07 3184 2290
      </li>
      <li>
        <svg viewBox="0 0 16 16" aria-hidden="true"><path d="M4.5 0h7a1 1 0 0 1 1 1v14a1 1 0 0 1-1 1h-7a1 1 0 0 1-1-1V1a1 1 0 0 1 1-1zm.6 2v10h5.8V2zM8 12.8a.9.9 0 1 0 0 1.8.9.9 0 0 0 0-1.8z"/></svg>
        0412 735 018
      </li>
      <li>
        <svg viewBox="0 0 16 16" aria-hidden="true"><path d="M4 1h8v4H4zM1 6h14v6h-2v-2H3v2H1zm3 5h8v4H4z"/></svg>
        07 3184 2291
      </li>
      <li>
        <svg viewBox="0 0 16 16" aria-hidden="true"><path d="M1 3h14v10H1zm1.5 1.2L8 8.6l5.5-4.4z"/></svg>
        hello@haventrix.com
      </li>
      <li>
        <svg viewBox="0 0 16 16" aria-hidden="true"><path d="M8 1a7 7 0 1 0 0 14A7 7 0 0 0 8 1zm-1 2.2c.6.8.4 1.6-.5 2.1-.9.5-.6 1.6.4 1.8 1 .2 1.4 1 1 2l-.6 2.6C5 11 3.2 9.2 3.2 7c0-1.7 1.5-3.4 3.8-3.8zm3.6 1c1.3.9 2.2 2.2 2.2 3.8l-1.6-.6-.9-1.6z"/></svg>
        www.haventrix.com
      </li>
    </ul>

    <div class="nameplate">
      <p class="nameplate__name">LIAM CARTWRIGHT</p>
      <p class="nameplate__role">CEO/FOUNDER</p>
    </div>
  </section>

  <section class="card card--back">
    <div class="brand">
      <span class="brand__dot"></span>
      <span class="brand__name">HAVENTRIX</span>
    </div>
  </section>
</body>
</html>
```